Label Design VelmoRest Capsules

Hello dear designers!

We run a brand for dietary supplements and are looking for a talented designer to help take our brand to the next level. We are planning to launch new products with fresh packaging and redesigned labels. Additionally, we would like to refresh our company logo to make it fit better on the packaging.

Important Info:

Our brand: VelmoPure – specializing in products for detoxification, sleep, and eye protection.
Our shop: www.velmopure.at – currently offering two main products:
VelmoPure (Detox Tincture)
Velmo Optic Guard (Blue Light Filter Glasses)
Project Goal: Initially, we are looking for a label design for our new product VelmoRest (sleep capsules). If we like the design, we would like to revise the label for our first product, VelmoPure, and potentially rework our logo to make it more compact and visually appealing on our packaging.

Design Preferences: We are fans of the design style of Farv Nutra and would love a design in a similar style – modern, clean, and premium – but with a unique touch that fits our brand. You will find some inspirations and ideas that we particularly like in the attachment.

Important:

Our packaging for VelmoRest is an 8 OZ jar (similar to the smaller jars used by Farv Nutra).
The label should be clear, appealing, and give the product a high-quality look.
An example of a previous design draft (which hasn’t fully convinced us yet), along with inspirations for our upcoming bundle (including VelmoPure, VelmoRest, and VelmoOptic Guard), is also attached.
Special Opportunity: The designer with the best concept will have the chance to collaborate with us long-term! We have two more brands in the pipeline and are looking for a reliable and creative partner for future projects. Generous compensation and tips are guaranteed.

We look forward to seeing creative and professional designs that will take our brand to the next level!

Target Market(s)

Germany

Industry/Entity Type

Supplement

Font styles to use
Sans Serif

Colors

Designer to choose colors to be used in the design.

Requirements
Must have
• Es sollte Hochwertig und Modern aussehen. Matt schwarzer hintergrund. less is more
Nice to have
• Maybe The head should be visible in the background.
Should not have
• it should not be colorful, and not too playful, it should definitely not look cheap!

```html
<!DOCTYPE html>
<html lang="de">
<head>
<meta charset="utf-8">
<title>VelmoRest Label</title>
<link rel="stylesheet" href="https://fonts.googleapis.com/css2?family=Montserrat:ital,wght@0,500;1,700;1,800&family=Oswald:wght@400;500;600&display=swap">
<style>
  :root {
    --page: #efefef;
    --ink: #0b0b0c;
    --ink-soft: #1c1c1e;
    --sky: #5cc3e3;
    --sky-deep: #3aa6cd;
    --sky-light: #8ad8ef;
    --white: #f4f6f7;
    --band-text: rgba(255,255,255,0.75);
  }
  * { box-sizing: border-box; margin: 0; padding: 0; }
  html, body { width: 1200px; height: 800px; overflow: hidden; background: var(--page); }
  .label {
    position: absolute; left: 220px; top: 50px; width: 760px; height: 700px;
    background: var(--ink); overflow: hidden; border-radius: 6px;
    font-family: "Oswald", sans-serif;
  }
  .texture {
    position: absolute; left: 0; top: 60px; width: 100%; height: 560px;
    background: radial-gradient(ellipse at 25% 45%, #3a3a3c 0%, #1a1a1b 40%, var(--ink) 75%);
  }
  .band {
    position: absolute; left: 0; width: 100%;
    background: linear-gradient(90deg, var(--sky-light), var(--sky) 45%, var(--sky-deep));
  }
  .band--top { top: 0; height: 70px; }
  .band--bottom { top: 600px; height: 100px; }
  .ticker {
    position: absolute; left: 0; width: 100%; display: flex; justify-content: space-around;
    font-size: 11px; letter-spacing: 1px; color: var(--band-text); font-weight: 500;
  }
  .band--top .ticker { top: 24px; }
  .band--bottom .ticker { top: 78px; }
  .brand-tab {
    position: absolute; left: 230px; top: 60px; width: 300px; height: 145px;
    background: linear-gradient(90deg, var(--sky-light), var(--sky) 50%, var(--sky-deep));
    border-radius: 0 0 44px 44px;
    display: flex; flex-direction: column; align-items: center; justify-content: center; gap: 14px;
  }
  .brand-dot { width: 46px; height: 46px; border: 2px solid var(--white); border-radius: 50%; }
  .brand-name {
    font-family: "Montserrat", sans-serif; font-weight: 500; font-size: 24px;
    letter-spacing: 5px; color: var(--white);
  }
  .title {
    position: absolute; top: 250px; width: 100%; text-align: center;
    font-family: "Montserrat", sans-serif; font-style: italic; font-weight: 800;
    font-size: 66px; color: var(--white); letter-spacing: 1px;
  }
  .tagline {
    position: absolute; top: 338px; width: 100%; text-align: center;
    font-family: "Montserrat", sans-serif; font-style: italic; font-weight: 700;
    font-size: 21px; color: var(--sky); letter-spacing: 0.5px;
  }
  .benefits {
    position: absolute; top: 395px; left: 0; width: 100%;
    display: flex; justify-content: center; gap: 22px;
  }
  .benefit { width: 108px; text-align: center; color: var(--white); font-size: 10px; line-height: 1.5; font-weight: 500; }
  .benefit svg { width: 48px; height: 48px; display: block; margin: 0 auto 14px; }
  .count {
    position: absolute; top: 505px; width: 100%; text-align: center;
    font-size: 76px; font-weight: 600; color: var(--sky); line-height: 1;
  }
  .unit-tab {
    position: absolute; left: 295px; top: 588px; width: 170px; height: 76px;
    background: var(--ink); border-radius: 28px;
    display: flex; align-items: center; justify-content: center;
    font-size: 34px; font-weight: 500; color: var(--white);
  }
  .servings, .purpose {
    position: absolute; top: 620px; font-size: 26px; font-weight: 500; color: var(--white);
  }
  .servings { left: 92px; letter-spacing: 3px; }
  .purpose { left: 478px; }
</style>
</head>
<body>
  <div class="label">
    <div class="texture" role="img" aria-label="Dunkles organisches Labyrinthmuster als Hintergrundstruktur"></div>

    <div class="band band--top">
      <div class="ticker"><span>DIETARY SUPPLEMENT</span><span>DIETARY SUPPLEMENT</span><span>DIETARY SUPPLEMENT</span><span>DIETARY SUPPLEMENT</span><span>DIETARY SUPPLEMENT</span></div>
    </div>

    <div class="brand-tab">
      <span class="brand-dot"></span>
      <span class="brand-name">VELMOPURE</span>
    </div>

    <h1 class="title">VELMO REST</h1>
    <p class="tagline">FÖRDERT DIE TIEFSCHLAFPHASE</p>

    <div class="benefits">
      <div class="benefit">
        <svg viewBox="0 0 48 48" fill="none" stroke="var(--sky)" stroke-width="3">
          <path d="M30 8a16 16 0 1 0 12 24A13 13 0 0 1 30 8z" fill="var(--sky)"/>
        </svg>
        ZWISCHENÜBERSCHRIFT<br>HINZUFÜGEN
      </div>
      <div class="benefit">
        <svg viewBox="0 0 48 48" fill="var(--sky)">
          <path d="M24 6c6 8 6 18 0 28c-6-10-6-20 0-28z"/>
          <path d="M6 22c9 0 15 5 17 13c-9 0-15-5-17-13z"/>
          <path d="M42 22c-9 0-15 5-17 13c9 0 15-5 17-13z"/>
        </svg>
        ZWISCHENÜBERSCHRIFT<br>HINZUFÜGEN
      </div>
      <div class="benefit">
        <svg viewBox="0 0 48 48" fill="none" stroke="var(--sky)" stroke-width="3">
          <circle cx="24" cy="24" r="18"/>
          <path d="M27 11l-9 15h7l-4 11l10-16h-7z" fill="var(--sky)" stroke="none"/>
        </svg>
        ZWISCHENÜBERSCHRIFT<br>HINZUFÜGEN
      </div>
    </div>

    <div class="count">60</div>

    <div class="band band--bottom">
      <div class="ticker"><span>DIETARY SUPPLEMENT</span><span>DIETARY SUPPLEMENT</span><span>DIETARY SUPPLEMENT</span><span>DIETARY SUPPLEMENT</span><span>DIETARY SUPPLEMENT</span></div>
    </div>
    <span class="servings">30 PORTIONEN</span>
    <div class="unit-tab">KAPSELN</div>
    <span class="purpose">NACHT-ERGÄNZUNG</span>
  </div>
</body>
</html>
```